HollowPine Ventures Inc. Business Card Design

My business is custom renovations and homes.I would need to have a new business logo created to go along with my company name. The business card should be of a modern style as this is the market I am focused on. I would need my contact information and website posted on the card. I would also like to list a few of the tasks I conduct on the card (such as: Renovations, Additions, Repairs, New Homes, Design, Consultations). On the reverse of the card I currently have just my logo and my motto, "Shaping A Bold Path". However, I am open to completely changing everything as I am starting a new year and would like to excel further. Any new ideas and suggestions are always welcomed. Thank you.

Target Market(s)

Upscale residential and commercial renovations and builds

Industry/Entity Type

Business

Contact Information for Business Card

I would like the design to be able to be laser cut or burnt onto a wooden business card. I will be creating one option of cards for really loyal customers (wooden) and a second option for the everyday customer (paper).

Font styles to use
Other font styles liked:
• Calibri / anything of mordern taste

Colors
f37122
5c5c5c
474747
ffffff

Requirements
Must have
• I would like the colours of my business to be a sharp orange and grey. I believe this will symbolize a modern style. I am open to other suggestions if this is not suitable for the designers tastes. My contact info as follows:
• Will Marsh
• President
• HollowPine Ventures Inc.
• 555-214-3987
• will@hollowpineventures.example
• I would like my website (currently under construction) hollowpineventures.example on the card aswell.
Nice to have
• Along with a modern logo representing HollowPine, I would like something on the card besides the logo and contact information. Perhaps a small background design. I feel it may be nice to have my services listed on the card (in smaller font on the bottom) Renovations, Additions, Repairs, Design, Consultations.
Should not have
• The business card should not have too many different colors. Should not have rounded corners.

```html
<!DOCTYPE html>
<html lang="en">
<head>
<meta charset="utf-8">
<title>HollowPine Ventures Inc. — Business Card</title>
<link href="https://fonts.googleapis.com/css2?family=Open+Sans:wght@400;600;700;800&display=swap" rel="stylesheet">
<style>
  :root{
    --orange:#f37122;
    --orange-deep:#ef6a1f;
    --grey:#5c5c5c;
    --grey-dark:#474747;
    --white:#ffffff;
    --stage:#2a2a2a;
  }
  *{box-sizing:border-box;margin:0;padding:0}
  html,body{width:1200px;height:900px;overflow:hidden}
  body{
    background:var(--stage);
    font-family:"Open Sans",Calibri,Arial,sans-serif;
    position:relative;
  }
  .card{
    position:absolute;
    width:600px;height:343px;
    overflow:hidden;
    background:var(--white);
  }

  /* ---------- Back of card ---------- */
  .card--back{left:300px;top:60px}
  .back__band-top{position:absolute;left:0;top:0;width:100%;height:30px;background:var(--grey)}
  .back__band-bottom{position:absolute;left:0;bottom:0;width:100%;height:62px;background:var(--grey)}
  .back__rule{position:absolute;left:0;bottom:72px;width:100%;height:4px;background:var(--orange)}
  .back__brand{
    position:absolute;left:0;right:0;top:92px;text-align:center;
    font-weight:800;font-size:56px;line-height:1.2;color:var(--orange);letter-spacing:-1px;
  }
  .back__company{
    position:absolute;left:0;right:0;top:176px;text-align:center;
    font-weight:600;font-size:22px;color:var(--grey-dark);letter-spacing:3px;
  }
  .back__web{
    position:absolute;left:0;right:0;bottom:19px;text-align:center;
    font-size:17px;color:var(--white);letter-spacing:3.5px;
  }

  /* ---------- Front of card ---------- */
  .card--front{left:300px;top:480px}
  .front__panel{
    position:absolute;left:0;top:0;width:282px;height:100%;
    background:linear-gradient(180deg,var(--orange) 0%,var(--orange-deep) 100%);
  }
  .front__band{position:absolute;left:0;bottom:0;width:100%;height:24px;background:var(--orange-deep)}
  .front__line{position:absolute;left:0;bottom:32px;width:282px;height:3px;background:var(--white)}
  .front__name{
    position:absolute;left:30px;top:60px;
    font-weight:800;font-size:38px;color:var(--white);letter-spacing:.5px;line-height:1;
  }
  .front__title{
    position:absolute;left:52px;top:104px;
    font-weight:700;font-size:17px;color:var(--white);letter-spacing:1px;
  }
  .contact{position:absolute;left:22px;top:170px;list-style:none}
  .contact__item{
    display:flex;align-items:center;gap:9px;
    font-size:12.5px;color:var(--white);margin-bottom:12px;white-space:nowrap;
  }
  .contact__icon{width:26px;height:26px;flex:none}
  .front__brand{
    position:absolute;left:282px;right:0;top:100px;text-align:center;
    font-weight:800;font-size:44px;line-height:1.2;color:var(--orange);letter-spacing:-1px;
  }
  .services{
    position:absolute;left:282px;right:0;top:176px;text-align:center;
    font-size:13px;color:var(--grey-dark);line-height:1.5;
  }
</style>
</head>
<body>

<section class="card card--back" aria-label="Card back">
  <div class="back__band-top"></div>
  <div class="back__brand">HollowPine</div>
  <div class="back__company">HollowPine Ventures Inc.</div>
  <div class="back__rule"></div>
  <div class="back__band-bottom"></div>
  <div class="back__web">hollowpineventures.example</div>
</section>

<section class="card card--front" aria-label="Card front">
  <div class="front__panel"></div>
  <div class="front__band"></div>
  <div class="front__line"></div>

  <h1 class="front__name">Will Marsh</h1>
  <div class="front__title">PRESIDENT</div>

  <ul class="contact">
    <li class="contact__item">
      <svg class="contact__icon" viewBox="0 0 26 26" aria-hidden="true">
        <circle cx="13" cy="13" r="11.5" fill="none" stroke="#fff" stroke-width="1.5"/>
        <path d="M8.5 9.5c0-.8.6-1.3 1.3-1.3h1.3l1 2.4-1.1 1a7 7 0 0 0 3.4 3.4l1-1.1 2.4 1v1.3c0 .7-.5 1.3-1.3 1.3A8 8 0 0 1 8.5 9.5z" fill="#fff"/>
      </svg>
      555-214-3987
    </li>
    <li class="contact__item">
      <svg class="contact__icon" viewBox="0 0 26 26" aria-hidden="true">
        <circle cx="13" cy="13" r="11.5" fill="none" stroke="#fff" stroke-width="1.5"/>
        <rect x="7.5" y="9" width="11" height="8" fill="none" stroke="#fff" stroke-width="1.3"/>
        <path d="M7.5 9l5.5 4.5L18.5 9" fill="none" stroke="#fff" stroke-width="1.3"/>
      </svg>
      will@hollowpineventures.example
    </li>
    <li class="contact__item">
      <svg class="contact__icon" viewBox="0 0 26 26" aria-hidden="true">
        <circle cx="13" cy="13" r="11.5" fill="none" stroke="#fff" stroke-width="1.5"/>
        <circle cx="13" cy="13" r="6" fill="none" stroke="#fff" stroke-width="1.2"/>
        <ellipse cx="13" cy="13" rx="2.6" ry="6" fill="none" stroke="#fff" stroke-width="1.1"/>
        <path d="M7 13h12M8 10h10M8 16h10" stroke="#fff" stroke-width="1"/>
      </svg>
      www.hollowpineventures.example
    </li>
  </ul>

  <div class="front__brand">HollowPine</div>
  <p class="services">Renovations | Additions | Repairs |<br>Design | Consultations</p>
</section>

</body>
</html>
```